Property Management Company Business Cards

Need business cards for a property management company located in Michigan. We manage houses for clients all over the world. Young and modern company, looking for eye catching design. Please work with the attached logo.

Industry/Entity Type

Property Management

Requirements
Must have
• Need lines for address, telephone number, fax number, web site.

Also lines for name, and job title

```html
<!DOCTYPE html>
<html lang="en">
<head>
<meta charset="utf-8">
<title>Lakeshore Harbor Management – Business Card</title>
<link rel="stylesheet" href="https://fonts.googleapis.com/css2?family=Cinzel:wght@400&display=swap">
<style>
  :root {
    --navy: #0c1232;
    --ink: #ffffff;
    --brand-blue: #29a8e0;
    --mark-grey: #3d3d42;
    --sphere-light: #78748c;
    --sphere-mid: #67637c;
    --sphere-edge: #3c3a55;
  }
  * { margin: 0; padding: 0; box-sizing: border-box; }
  html, body {
    width: 1200px;
    height: 776px;
    overflow: hidden;
    background: var(--navy);
  }
  .card {
    position: relative;
    width: 1200px;
    height: 776px;
    background: var(--navy);
    overflow: hidden;
    font-family: "Cinzel", serif;
    color: var(--ink);
  }
  .sphere {
    position: absolute;
    left: 0;
    top: 0;
    width: 1200px;
    height: 776px;
  }
  .brand {
    position: absolute;
    left: 33px;
    top: 33px;
    display: flex;
    align-items: center;
    gap: 40px;
  }
  .brand-dot {
    width: 194px;
    height: 194px;
    border-radius: 50%;
    background: var(--mark-grey);
    flex: none;
  }
  .brand-name {
    color: var(--brand-blue);
    font-weight: 400;
    line-height: 1;
  }
  .brand-name .line-main {
    display: block;
    font-size: 62px;
    letter-spacing: 1px;
  }
  .brand-name .line-sub {
    display: block;
    margin-top: 18px;
    font-size: 40px;
    letter-spacing: 38px;
  }
  .address {
    position: absolute;
    left: 0;
    width: 1380px;
    top: 287px;
    text-align: center;
    font-size: 31px;
    line-height: 43px;
    letter-spacing: 0.5px;
  }
  .contact {
    position: absolute;
    left: 29px;
    top: 476px;
    font-size: 30px;
    line-height: 36px;
  }
  .contact .phones { margin-top: 36px; }
  .website {
    position: absolute;
    left: 0;
    width: 1200px;
    top: 710px;
    text-align: center;
    font-size: 31px;
    letter-spacing: 0.5px;
  }
</style>
</head>
<body>
  <main class="card">
    <svg class="sphere" viewBox="0 0 1200 776" aria-hidden="true">
      <defs>
        <radialGradient id="sphere-shade" cx="0.62" cy="0.45" r="0.6">
          <stop offset="0" stop-color="var(--sphere-light)"/>
          <stop offset="0.7" stop-color="var(--sphere-mid)"/>
          <stop offset="1" stop-color="var(--sphere-edge)"/>
        </radialGradient>
      </defs>
      <circle cx="1147" cy="813" r="418" fill="url(#sphere-shade)"/>
    </svg>

    <header class="brand">
      <span class="brand-dot" aria-hidden="true"></span>
      <h1 class="brand-name">
        <span class="line-main">LAKESHORE HARBOR</span>
        <span class="line-sub">MANAGEMENT</span>
      </h1>
    </header>

    <p class="address">18420 Maple Crest Rd, Livonia,<br>Michigan, 48152</p>

    <section class="contact">
      <p class="person-name">NAME</p>
      <p class="person-title">POSITION</p>
      <div class="phones">
        <p class="phone">T: 734-555-0148</p>
        <p class="fax">F: 734-555-0149</p>
      </div>
    </section>

    <p class="website">WWW.LAKESHOREHARBOR.COM</p>
  </main>
</body>
</html>
```